Supplement Company Needs a Protein Powder Pouch Design

We are looking for a modern and fresh design for our 500g pouches of protein powder as our current design is not eye catching or exciting enough.

This new design will be printed on both sides of a 178mm x 280mm x 101mm pouch.

We have 4 flavours. These are Banana Ice Cream, Chocolate Deluxe, Strawberries & Cream and Vanilla Ice Cream.

Industry/Entity Type

Supplement

Requirements
Must have
• Attractive and eye catching front and space for all the nutritional information and ingredients on the back.

Must clearly state 'food supplement' somewhere on the front of the pouch.
Nice to have
• Our logo is attached.
Should not have
• No health claims as these are not allowed in the UK

```html
<!DOCTYPE html>
<html lang="en">
<head>
<meta charset="utf-8">
<title>Brisk Supplements – Protein Powder Pouch Front</title>
<link href="https://fonts.googleapis.com/css2?family=Oswald:wght@500;600;700&family=Roboto+Condensed:wght@400;700&display=swap" rel="stylesheet">
<style>
  :root {
    --backdrop: #f1f1f1;
    --pouch: #1c1c1e;
    --white: #f4f4f4;
    --coral: #ef5a5b;
    --red: #d8363a;
    --rule: #bdbdbd;
  }
  html, body {
    margin: 0;
    padding: 0;
    width: 1200px;
    height: 1078px;
    overflow: hidden;
    background: var(--backdrop);
  }
  .canvas {
    position: relative;
    width: 1200px;
    height: 1078px;
  }
  .pouch-front {
    position: absolute;
    left: 352px;
    top: 163px;
    width: 500px;
    height: 831px;
    background: var(--pouch);
    border-radius: 4px;
    overflow: hidden;
  }
  .brand {
    position: absolute;
    left: 0;
    top: 138px;
    width: 100%;
    text-align: center;
    color: var(--white);
  }
  .brand-name {
    font-family: "Oswald", sans-serif;
    font-weight: 700;
    font-size: 56px;
    line-height: 1;
    letter-spacing: 0.01em;
  }
  .brand-tag {
    font-family: "Oswald", sans-serif;
    font-weight: 700;
    font-size: 11px;
    line-height: 1;
    letter-spacing: 0.55em;
    padding-left: 0.55em;
    margin-top: 6px;
  }
  .title-stack {
    position: absolute;
    left: 0;
    top: 0;
    width: 500px;
    height: 831px;
    margin: 0;
  }
  .title-stack text {
    font-family: "Oswald", sans-serif;
    text-transform: uppercase;
  }
  .title-protein { fill: var(--coral); font-weight: 700; font-size: 94px; }
  .title-powder { fill: var(--white); font-weight: 700; font-size: 101px; }
  .title-category { fill: var(--white); font-weight: 500; font-size: 41px; }
  .flavour {
    position: absolute;
    left: 277px;
    top: 566px;
    width: 137px;
  }
  .flavour-rule {
    height: 0;
    border-top: 1.5px solid var(--rule);
    margin-bottom: 8px;
  }
  .flavour-name {
    font-family: "Roboto Condensed", sans-serif;
    font-weight: 400;
    font-size: 22px;
    line-height: 25px;
    color: var(--red);
  }
  .facts {
    position: absolute;
    left: 125px;
    top: 655px;
    display: flex;
    gap: 12px;
  }
  .fact {
    box-sizing: border-box;
    width: 72px;
    height: 72px;
    border: 1.5px solid var(--white);
    color: var(--white);
    text-align: center;
    font-family: "Roboto Condensed", sans-serif;
    padding-top: 8px;
  }
  .fact-protein {
    background: var(--red);
    border-color: var(--red);
    margin-left: 5px;
  }
  .fact-value {
    font-weight: 700;
    font-size: 30px;
    line-height: 32px;
  }
  .fact-unit { font-size: 18px; }
  .fact-label {
    font-weight: 700;
    font-size: 7.5px;
    line-height: 9px;
    letter-spacing: 0.04em;
    text-transform: uppercase;
  }
  .net-weight {
    position: absolute;
    left: 198px;
    top: 746px;
    font-family: "Roboto Condensed", sans-serif;
    font-weight: 700;
    font-size: 14px;
    letter-spacing: 0.14em;
    color: var(--white);
  }
</style>
</head>
<body>
<div class="canvas">
  <section class="pouch-front" aria-label="Protein powder pouch, front panel">
    <header class="brand">
      <div class="brand-name">BRISK</div>
      <div class="brand-tag">SUPPLEMENTS</div>
    </header>

    <svg class="title-stack" viewBox="0 0 500 831" role="heading" aria-level="1" aria-label="Protein Powder Food Supplement">
      <text class="title-protein" transform="translate(145 626) rotate(-90)" textLength="340" lengthAdjust="spacing">Protein</text>
      <text class="title-powder" transform="translate(231 626) rotate(-90)" textLength="347" lengthAdjust="spacing">Powder</text>
      <text class="title-category" transform="translate(268 626) rotate(-90)" textLength="304" lengthAdjust="spacing">Food Supplement</text>
    </svg>

    <div class="flavour">
      <div class="flavour-rule"></div>
      <div class="flavour-name">Strawberries<br>&amp; Cream</div>
    </div>

    <div class="facts">
      <div class="fact">
        <div class="fact-value">117</div>
        <div class="fact-label">Calories<br>per serving</div>
      </div>
      <div class="fact">
        <div class="fact-value">16</div>
        <div class="fact-label">Servings</div>
      </div>
      <div class="fact fact-protein">
        <div class="fact-value">21<span class="fact-unit">G</span></div>
        <div class="fact-label">Protein</div>
      </div>
    </div>

    <div class="net-weight">NET WT 500g</div>
  </section>
</div>
</body>
</html>
```